Tech Laundry service company looking for a new modern and clean web site

Our site is www.brisklinenhub.com we are looking to rebrand our whole website.

We offer free pickup and delivery for laundry and dry cleaning in the NYC area. we target residential customers.

Sites to compare are www.trypolvex.com and www.zentumo.com
Most content can be found at www.brisklinenhub.com

We are looking for a clean and modern look. Nothing to busy

colors and font we use are
Logo font: Harabara
Slogan font: Swiss 721 Light Extended BT

Dark blue: C 100 M 88 Y 0 K 0
Light blue: C 85 M 50 Y 0 K 0
Orange: C 0 M 80 Y 95 K 0

Violet: C 85 M 100 Y 0 K 0

We use only Marlo, Quilse and vendrax
We are provide eco-friendly
next day laundry service

Our mission Statement is to deliver the Cleanest and Brightest clothes in the market. we use only top of the line

"We are the #1 proud supporter of Marlo and Quilse"

There will be 4 pages
the home page
and a 2 page scheduling page

THE HOME PAGE-
navigation bar must include

Home,
Clean my Clothes (schedule a pickup)
Pricing
Blog
Service Area
Commercial/Wholesale
Sign in
must have key elements about our business such as:
1. Our Price is 1.10 a lb
2. "New customers get 50% off first order and 100% off second order!"
3. we have next day service on all laundry orders
Again, you can pull the content off our current website brisklinenhub.com

Order Page-

Attached please find 5 steps of the ordering page. We are looking to condense into 2
we want step2+step3+step4 on one page
then step1+step5 on the second page on step5 we want the coinbird logo attached as well (as we do all credit card processing through CoinBird)
at the end of the process we want to offer them to create a password to auto register
the order confirmation is attached as well. we need all that info but would like it to seem cleaner and modern.

PRICING PAGE-

Wash and Fold 1.10 per Lb ($27 min charge)
Blankets $12 and up
Bathroom Rugs $5.00 and up

Dry Cleaning
Launder and Press shirt 1.25
Suit Jacket 6.00
Pants and Skirts 6.00
2 pc suit 12.00
Dress 10.00 and up
Blouses & Sweaters 6.00

Again, we are looking for a clean and sleek site not to busy.

Based on this we will be needed another 6-8 pages of design work that will be negotiated with the winner at the end of this contest.
Good Luck!

Target Market(s)

our customers are between the ages of 22-40 years old all live in NYC

Industry/Entity Type

Dry Cleaning

Number of Pages Required

4 page

Font styles to use
Other font styles liked:
• Harabara

Requirements
Must have
• sleek and cool design
• see www.polvex.com and zentumo.com for concept
• Our current site is brisklinenhub.com which we are looking to rebrand
Nice to have
• colors and font we use are
• Logo font: Harabara
• Slogan font: Swiss 721 Light Extended BT
• Dark blue: C 100 M 88 Y 0 K 0
• Light blue: C 85 M 50 Y 0 K 0
• Orange: C 0 M 80 Y 95 K 0
• Violet: C 85 M 100 Y 0 K 0
Should not have
• we want all the colors to be uniform. we are sending a message that we are the brightest and cleanest laundry service in the city!

```html
<!DOCTYPE html>
<html lang="en">
<head>
<meta charset="utf-8">
<title>eRinsely.com – NYC Laundry Pickup &amp; Delivery</title>
<link rel="stylesheet" href="https://fonts.googleapis.com/css2?family=Roboto:ital,wght@0,400;0,500;0,700;1,400&family=Open+Sans:wght@400;600&display=swap">
<style>
:root{
  --blue:#1e9ad6;
  --blue-dark:#1a64b0;
  --heading-blue:#1b6bb7;
  --footer-left:#3b7ec6;
  --footer-right:#5ea3dc;
  --orange:#ef5a1e;
  --ink:#222;
  --body:#444;
  --grey-band:#e9e9e9;
  --logo-grey:#8a8a8a;
  --white:#fff;
}
*{box-sizing:border-box;margin:0;padding:0}
html,body{width:1200px;height:2330px;overflow:hidden;background:var(--white)}
body{position:relative;font-family:"Open Sans",Arial,sans-serif;color:var(--body)}

.site-header{position:absolute;top:0;left:0;width:1200px;height:136px}
.brand{position:absolute;left:98px;top:28px;width:130px;text-align:center}
.brand-mark{width:42px;height:42px;border-radius:50%;background:var(--blue);margin:0 auto 6px}
.brand-name{font-family:"Roboto",Arial,sans-serif;font-weight:700;font-size:21px;color:var(--blue-dark);line-height:1}
.brand-tagline{font-size:8px;color:var(--orange);margin-top:3px;letter-spacing:.5px}
.header-phone{position:absolute;right:75px;top:22px;font-family:"Roboto",Arial,sans-serif;font-weight:500;font-size:20px;color:var(--ink)}
.main-nav{position:absolute;right:85px;top:78px;display:flex;align-items:center;gap:34px;font-family:"Roboto",Arial,sans-serif;font-size:15.5px;color:var(--ink)}
.sign-in{background:var(--blue);color:var(--white);border-radius:18px;padding:8px 20px;font-size:15px;margin-left:-6px}

.hero{position:absolute;top:136px;left:0;width:1200px;height:528px;background:linear-gradient(100deg,#8c2b2b 0%,#b8303a 18%,#2b3f7a 34%,#d9b23a 46%,#a8402f 58%,#dde2e8 72%,#b7c4d2 100%)}
.hero-shade{position:absolute;inset:0;background:linear-gradient(180deg,rgba(0,0,0,.15),rgba(0,0,0,.05) 60%,rgba(0,0,0,.2))}
.hero-title{position:absolute;left:70px;top:314px;font-family:"Roboto",Arial,sans-serif;font-weight:700;font-size:43px;line-height:46px;color:var(--white);text-transform:uppercase}

.features{position:absolute;top:720px;left:74px;display:flex;gap:27px}
.feature-tile{position:relative;width:332px;height:333px}
.feature-tile .tile-photo{position:absolute;inset:0}
.tile-delivery .tile-photo{background:linear-gradient(135deg,#9fb2c2,#6a5a4e 55%,#3d3530)}
.tile-pickup .tile-photo{background:linear-gradient(135deg,#7a6a58,#c9b8a6 50%,#b9323a)}
.tile-price .tile-photo{background:linear-gradient(135deg,#1f2a20,#6f8aa0 50%,#2f6a2a)}
.feature-tile h2{position:absolute;left:16px;bottom:18px;font-family:"Roboto",Arial,sans-serif;font-weight:500;font-size:42px;line-height:46px;color:var(--white)}

.customers{position:absolute;top:1100px;left:0;width:1200px;text-align:center}
.customers h3{font-family:"Roboto",Arial,sans-serif;font-weight:500;font-size:21px;color:var(--ink)}
.customer-list{display:flex;justify-content:space-between;width:930px;margin:60px auto 0;list-style:none;font-family:"Roboto",Arial,sans-serif;font-weight:700;font-size:22px;color:var(--logo-grey);letter-spacing:1px}

.about{position:absolute;top:1274px;left:0;width:1200px;height:357px;background:var(--grey-band)}
.about-col{position:absolute;top:34px;width:338px}
.about-col:nth-child(1){left:72px}
.about-col:nth-child(2){left:431px}
.about-col:nth-child(3){left:792px}
.about-col h2{font-family:"Roboto",Arial,sans-serif;font-weight:500;font-size:22px;line-height:26px;color:var(--heading-blue);margin-bottom:16px}
.about-col p{font-size:13.3px;line-height:20px;color:var(--body)}
.about-col p+p{margin-top:18px}

.testimonial{position:absolute;top:1686px;left:0;width:1200px;text-align:center}
.avatar{width:98px;height:98px;margin:0 auto}
.testimonial blockquote{margin-top:36px;font-family:"Roboto",Arial,sans-serif;font-style:italic;font-size:24px;line-height:33px;color:#555;letter-spacing:.6px}
.testimonial cite{display:block;margin-top:30px;font-style:normal;font-family:"Roboto",Arial,sans-serif;font-size:18px;color:var(--orange);letter-spacing:.5px}

.site-footer{position:absolute;top:1973px;left:0;width:1200px;height:307px;color:var(--white);font-family:"Roboto",Arial,sans-serif}
.footer-left{position:absolute;left:0;top:0;width:598px;height:307px;background:var(--footer-left)}
.footer-right{position:absolute;left:598px;top:0;width:602px;height:307px;background:var(--footer-right)}
.footer-block{position:absolute}
.footer-block h4{font-weight:500;font-size:21px;margin-bottom:10px}
.footer-block p{font-family:"Open Sans",Arial,sans-serif;font-size:13px;line-height:21px}
.contact{left:72px;top:34px}
.services{left:280px;top:34px}
.services strong{display:block;font-family:"Open Sans",Arial,sans-serif;font-weight:600;font-size:14px;margin-bottom:6px}
.badges{position:absolute;left:72px;top:178px;display:flex;gap:8px}
.badge{width:94px;height:94px;border-radius:50%;background:var(--white);border:4px solid #2b2b2b}
.badge+.badge{border-color:#1d4f8f}
.address{left:78px;top:28px}
.address h4{display:flex;align-items:center;gap:8px;margin-bottom:2px}
.address p{padding-left:28px}
.call{left:107px;top:104px}
.email{left:324px;top:98px}
.connect{left:107px;top:192px}
.social{display:flex;gap:7px;margin-top:4px}
.social span{width:31px;height:31px;border-radius:50%;border:2px solid var(--white)}
.legal{position:absolute;top:2280px;left:0;width:1200px;height:50px;text-align:center;line-height:50px;font-size:13px;color:#333}
</style>
</head>
<body>

<header class="site-header">
  <div class="brand">
    <div class="brand-mark"></div>
    <div class="brand-name">eRinsely.com</div>
    <div class="brand-tagline">Cleaner. Brighter. Faster.</div>
  </div>
  <div class="header-phone">(212) 555-0148</div>
  <nav class="main-nav">
    <span>Home</span><span>Clean My Clothes</span><span>Pricing</span><span>Blog</span><span>Service Area</span><span>Commercial/Wholesale</span><span class="sign-in">SIGN IN</span>
  </nav>
</header>

<section class="hero" role="img" aria-label="Photo of colourful shirts hanging on a clothes rail">
  <div class="hero-shade"></div>
  <h1 class="hero-title">We are the #1 proud<br>supporter of Marlo &amp; Quilse</h1>
</section>

<section class="features">
  <div class="feature-tile tile-delivery"><div class="tile-photo" role="img" aria-label="Photo of a happy couple at home"></div><h2>Next Day<br>Delivery</h2></div>
  <div class="feature-tile tile-pickup"><div class="tile-photo" role="img" aria-label="Photo of a courier handing a package to a customer at the door"></div><h2>Free Pickup<br>&amp; Delivery</h2></div>
  <div class="feature-tile tile-price"><div class="tile-photo" role="img" aria-label="Photo of cash being handed over"></div><h2>Only $1.10<br>a Pound?</h2></div>
</section>

<section class="customers">
  <h3>SOME OF OUR CUSTOMERS</h3>
  <ul class="customer-list">
    <li>NOVACAST</li><li>SKYVANE</li><li>GRIDLEAGUE</li><li>VOLTIC</li><li>BIG TOP TROUPE</li>
  </ul>
</section>

<section class="about">
  <article class="about-col">
    <h2>Join Thousands<br>of Satisfied New Yorkers</h2>
    <p>Brisk Linen Hub is NYC Laundry Delivery service at its best. Founded in 2008, our business has expanded to six locations and serves all of Manhattan! We offer free laundry delivery service for a set price of $1.10 per pound for residential and commercial customers.</p>
    <p>We also offer dry-cleaning services at great prices. You can call or schedule a pickup online and we'll pick it up on the same day. You won't find a laundry delivery service that's better than that!</p>
  </article>
  <article class="about-col">
    <h2>A Customized Commercial<br>Laundry Service</h2>
    <p>Our superior commercial laundry service is available for hotels, restaurants and a whole range of commercial customers. Among our past clients are Novacast, Skyvane, the Gridleague, Voltic Electronic, and Big Top Troupe Circus. Your laundry will be custom washed according to your preferences as well as professionally folded. All of our laundry is checked for quality assurance so that your business can maintain its high standards. If you're looking for a quality hotel or restaurant laundry service, come to Brisk Linen Hub!</p>
  </article>
  <article class="about-col">
    <h2>Laundry Pickup and Delivery<br>7 Days a Week</h2>
    <p>Laundry pickup and delivery shouldn't be a hassle. That's why we accept order online 24/7! The drivers at Brisk Linen Hub are on the road from 9am to 7pm to take care of our commitment of next day delivery. The service doesn't end here – if you have any questions or concerns, our superb customer service staff will address them immediately. When you come to Brisk Linen Hub, you're getting the best of the best in residential and commercial NYC laundry service.</p>
  </article>
</section>

<section class="testimonial">
  <svg class="avatar" viewBox="0 0 98 98" role="img" aria-label="Customer portrait">
    <rect x="19" y="19" width="60" height="60" transform="rotate(45 49 49)" fill="#fff" stroke="#cfcfcf" stroke-width="2"/>
    <circle cx="49" cy="49" r="30" fill="#c9a48a"/>
  </svg>
  <blockquote>“The detergent that you guys use smells so good!, I've gotten complements on<br>the smell!”</blockquote>
  <cite>Dana - Manhattan</cite>
</section>

<footer class="site-footer">
  <div class="footer-left">
    <div class="footer-block contact">
      <h4>Contact Us</h4>
      <p>Brisk Linen Hub<br>48 Harbor Lane, NY<br>NY, 10004, USA</p>
    </div>
    <div class="footer-block services">
      <h4>Service Features</h4>
      <strong>Convenient Laundry Service</strong>
      <p>24 Hour Turnaround.Free Pickup and<br>Delivery Easy Online Access</p>
    </div>
    <div class="badges"><span class="badge"></span><span class="badge"></span><span class="badge"></span></div>
  </div>
  <div class="footer-right">
    <div class="footer-block address">
      <h4><svg width="20" height="24" viewBox="0 0 20 24" aria-hidden="true"><path d="M10 1a8 8 0 0 0-8 8c0 6 8 14 8 14s8-8 8-14a8 8 0 0 0-8-8z" fill="none" stroke="#fff" stroke-width="2"/><circle cx="10" cy="9" r="3" fill="#fff"/></svg>Address</h4>
      <p>48 Harbor Lane, NY, NY, 10004, USA</p>
    </div>
    <div class="footer-block call"><h4>Call Us</h4><p>(212) 555-0148</p></div>
    <div class="footer-block email"><h4>Email Us</h4><p>orders@brisklinenhub.com</p></div>
    <div class="footer-block connect"><h4>Stay Connected</h4><div class="social" aria-hidden="true"><span></span><span></span><span></span><span></span></div></div>
  </div>
</footer>

<div class="legal">© 2015 eRinsely. All Rights Reserved &nbsp;•&nbsp; Terms and Conditions &nbsp;•&nbsp; Privacy Policy &nbsp;•&nbsp; Terms of Use</div>

</body>
</html>
```